PLUM BUSINESS CARD

Need a business card and logo. The company name is PLUM (Piedmont League of Ultimate Mareriders). It's a business that offers horseback riding lessons to young girls. Please put my name: Renata Bowley and a place for email and phone number. I would like the card to look feminine and soft. I like script type lettering. I want the card to be white or ivory with black or gray and hot pink print. A horse head outline would be cool, something whimsical. Think teen girl who likes glamour. Also, I give western riding lessons. So I like faded out background Images of western saddles, cowgirls, horses with long hair, ropes, horses in sunset...mabe the word PLUM can be made out of a lasso rope?

Just updated my project with a little more detail

Target Market(s)

Young girls/ cowgirls, western riding

Industry/Entity Type

Horseback Riding

Font styles to use
Script

Colors
e34197

Requirements
Must have
• A logo of PLUM.
Must say Piedmont League of Ultimate Mareriders
Colors are Pink and Black with an elegant, glamorous, feminine look.
Nice to have
• Could have a picture or outline of a horse

```html
<!DOCTYPE html>
<html lang="en">
<head>
<meta charset="utf-8">
<title>PLUM Business Card</title>
<link rel="stylesheet" href="https://fonts.googleapis.com/css2?family=Great+Vibes&family=Saira+Condensed:wght@300;700&display=swap">
<style>
  :root {
    --plum-night: #1c0820;
    --plum-deep: #5a0f4a;
    --magenta: #c0127a;
    --hot-pink: #e0409a;
    --blush: #e899a5;
    --frame: #8c1f5a;
    --label-pink: #cf6aa2;
    --cream: #f8e8e2;
    --ink: #111111;
    --rule: #ffffff;
  }
  html, body {
    margin: 0;
    padding: 0;
    width: 1200px;
    height: 722px;
    overflow: hidden;
    background: #ffffff;
  }
  .card {
    position: relative;
    width: 1200px;
    height: 722px;
    overflow: hidden;
  }
  .card__backdrop {
    position: absolute;
    inset: 0;
    background:
      radial-gradient(ellipse 520px 300px at 1130px 640px, var(--cream) 0%, rgba(248,232,226,0.6) 40%, rgba(248,232,226,0) 75%),
      radial-gradient(ellipse 300px 160px at 160px 720px, rgba(248,232,226,0.8) 0%, rgba(248,232,226,0) 80%),
      radial-gradient(ellipse 700px 420px at 820px 360px, var(--magenta) 0%, rgba(192,18,122,0.5) 45%, rgba(192,18,122,0) 80%),
      linear-gradient(135deg, var(--plum-deep) 0%, #7a1560 35%, #a0186e 60%, var(--plum-night) 100%);
  }
  .name-badge {
    position: absolute;
    left: 72px;
    top: 163px;
    width: 506px;
    height: 394px;
    box-sizing: border-box;
    background: var(--blush);
    border: 11px solid var(--frame);
    border-radius: 50%;
    display: flex;
    align-items: center;
    justify-content: center;
  }
  .name-badge__text {
    margin: 0;
    width: 380px;
    text-align: center;
    font-family: "Great Vibes", cursive;
    font-size: 44px;
    font-weight: 400;
    line-height: 1.2;
    color: var(--hot-pink);
  }
  .divider {
    position: absolute;
    left: 604px;
    top: 195px;
    width: 2px;
    height: 315px;
    background: var(--rule);
  }
  .contact-panel {
    position: absolute;
    left: 641px;
    top: 176px;
    width: 492px;
    height: 343px;
    box-sizing: border-box;
    background: var(--blush);
    border: 10px solid var(--frame);
    border-radius: 9px;
  }
  .contact-panel__name {
    position: absolute;
    left: 0;
    right: 0;
    top: 40px;
    text-align: center;
    font-family: "Great Vibes", cursive;
    font-size: 56px;
    line-height: 1;
    color: var(--hot-pink);
    margin: 0;
    font-weight: 400;
  }
  .contact-panel__fields {
    position: absolute;
    left: 28px;
    top: 140px;
    margin: 0;
    padding: 0;
    list-style: none;
    font-family: "Great Vibes", cursive;
    font-size: 32px;
    line-height: 53px;
    color: var(--label-pink);
  }
  .tagline {
    position: absolute;
    right: 21px;
    bottom: 18px;
    margin: 0;
    font-family: "Saira Condensed", "Arial Narrow", sans-serif;
    font-size: 50px;
    line-height: 1;
    white-space: nowrap;
  }
  .tagline__plain {
    font-weight: 300;
    color: var(--ink);
  }
  .tagline__accent {
    font-weight: 700;
    color: var(--hot-pink);
  }
</style>
</head>
<body>
  <main class="card">
    <div class="card__backdrop" role="img" aria-label="Deep plum to hot pink backdrop scattered with soft rounded square shapes, fading to cream at the lower right"></div>

    <div class="name-badge">
      <p class="name-badge__text">PLUM<br>Piedmont League of Ultimate Mareriders</p>
    </div>

    <div class="divider"></div>

    <section class="contact-panel">
      <h1 class="contact-panel__name">Renata Bowley</h1>
      <ul class="contact-panel__fields">
        <li>Tel.fax:</li>
        <li>Mobile:</li>
        <li>E-mail:</li>
      </ul>
    </section>

    <p class="tagline">
      <span class="tagline__plain">Western </span><span class="tagline__accent">Riding</span><span class="tagline__plain"> For </span><span class="tagline__accent">Beginners</span>
    </p>
  </main>
</body>
</html>
```